New Business Cards / Logo update

Logo:
can be updated but wanted pricing

New Business Cards:
take our existing business cards and upgrade them from a design perspective. We have two versions
Inside sales team does not have a cell phone and they use an appointment back slot.
Outside project managers and leadership uses a slogan backing and will have cell phones.

```html
<!DOCTYPE html>
<html lang="en">
<head>
<meta charset="utf-8">
<title>Hartwell Flooring – Business Cards</title>
<link rel="stylesheet" href="https://fonts.googleapis.com/css2?family=Crimson+Pro:ital,wght@0,400;1,400&family=Poppins:wght@400&display=swap">
<style>
  :root {
    --backdrop: #5e4731;
    --card: #ffffff;
    --brand-orange: #e08b22;
    --ink: #1a1614;
    --ink-soft: #7b7571;
    --watermark-warm: rgba(255, 255, 255, 0.13);
    --watermark-grey: #ebe9e6;
    --rule: #8c8986;
  }
  * { box-sizing: border-box; margin: 0; padding: 0; }
  html, body { width: 1200px; height: 2315px; overflow: hidden; }
  body { background: var(--backdrop); position: relative; font-family: "Poppins", sans-serif; }

  .card { position: absolute; background: var(--card); overflow: hidden; box-shadow: 0 3px 10px rgba(0,0,0,.35); }
  .card--front-a { left: 187px; top: 118px; width: 835px; height: 476px; }
  .card--back-slogan { left: 186px; top: 623px; width: 837px; height: 477px; background: var(--brand-orange); }
  .card--front-b { left: 186px; top: 1211px; width: 841px; height: 479px; }
  .card--back-appointment { left: 186px; top: 1720px; width: 843px; height: 480px; }

  /* front of card */
  .wordmark { position: absolute; left: 60px; top: 0; width: 315px; height: 100%; display: flex; align-items: center; justify-content: center; text-align: center;
    font-family: "Crimson Pro", serif; font-weight: 400; font-size: 62px; line-height: 1.1; color: var(--brand-orange); letter-spacing: .5px; }
  .divider { position: absolute; left: 381px; top: 144px; width: 2px; height: 190px; background: var(--brand-orange); }
  .contact { position: absolute; left: 431px; top: 134px; }
  .contact__name { font-family: "Crimson Pro", serif; font-size: 34px; line-height: 38px; color: var(--brand-orange); }
  .contact__role { font-family: "Crimson Pro", serif; font-size: 22px; line-height: 26px; color: var(--ink); }
  .contact__address { margin-top: 12px; font-size: 20px; line-height: 26px; color: var(--ink-soft); }
  .contact__lines { margin-top: 12px; font-size: 20px; line-height: 26px; color: var(--ink-soft); }
  .contact__line { display: flex; align-items: center; gap: 9px; }
  .contact__line svg { width: 16px; height: 16px; fill: var(--brand-orange); flex: none; }

  /* slogan back */
  .site-url { position: absolute; font-size: 24px; letter-spacing: 4.3px; }
  .card--back-slogan .site-url { left: 30px; top: 28px; color: #fff; }
  .watermark { position: absolute; font-family: "Crimson Pro", serif; font-style: italic; white-space: nowrap; line-height: 1; }
  .card--back-slogan .watermark { left: 30px; top: 90px; font-size: 110px; color: var(--watermark-warm); }
  .slogan { position: absolute; text-align: right; white-space: nowrap; }
  .slogan__lead { font-family: "Crimson Pro", serif; font-size: 86px; line-height: 1; margin-right: 14px; }
  .slogan__line { font-size: 44px; line-height: 52px; }
  .card--back-slogan .slogan { right: 47px; top: 300px; color: #fff; }
  .card--back-slogan .slogan__lead { color: var(--ink); }

  /* appointment back */
  .card--back-appointment .slogan { left: 43px; width: 520px; top: 36px; color: var(--ink-soft); }
  .card--back-appointment .slogan__lead { color: var(--brand-orange); }
  .card--back-appointment .watermark { left: 722px; top: 240px; font-size: 80px; color: var(--watermark-grey); transform: translate(-50%, -50%) rotate(-90deg); }
  .appointment { position: absolute; top: 356px; left: 43px; display: flex; font-size: 22px; color: var(--ink); }
  .appointment__field { display: flex; align-items: flex-end; gap: 14px; }
  .appointment__field + .appointment__field { margin-left: 45px; }
  .appointment__blank { width: 218px; height: 1px; background: var(--rule); margin-bottom: 6px; }
  .card--back-appointment .site-url { left: 43px; top: 424px; color: var(--brand-orange); letter-spacing: 3px; }
</style>
</head>
<body>

<section class="card card--front-a">
  <div class="wordmark">Hartwell Flooring</div>
  <div class="divider"></div>
  <div class="contact">
    <p class="contact__name">Dan Whitcombe</p>
    <p class="contact__role">Project Manager + Lead Estimator</p>
    <p class="contact__address">1450 Palm Grove Way<br>Lakeview, FL 34000</p>
    <div class="contact__lines">
      <p class="contact__line"><svg viewBox="0 0 16 16" aria-hidden="true"><path d="M4 0h8a1 1 0 0 1 1 1v14a1 1 0 0 1-1 1H4a1 1 0 0 1-1-1V1a1 1 0 0 1 1-1zm1 2v8h6V2zm1 10v2h4v-2z"/></svg>555 201 4830</p>
      <p class="contact__line"><svg viewBox="0 0 16 16" aria-hidden="true"><path d="M0 3h16v10H0zm1.5 1.2L8 9l6.5-4.8V4h-13zm0 1.6V12h13V5.8L8 10.6z"/></svg>dan@hartwellfloorco.com</p>
    </div>
  </div>
</section>

<section class="card card--back-slogan">
  <p class="site-url">hartwellfloorco.com</p>
  <p class="watermark">quality first</p>
  <div class="slogan">
    <p><span class="slogan__lead">Hartwell</span><span class="slogan__line">flooring at</span></p>
    <p class="slogan__line">an affordable price</p>
  </div>
</section>

<section class="card card--front-b">
  <div class="wordmark">Hartwell Flooring</div>
  <div class="divider"></div>
  <div class="contact">
    <p class="contact__name">Renata Ellison</p>
    <p class="contact__role">General Manager</p>
    <p class="contact__address">1450 Palm Grove Way<br>Lakeview, FL 34000</p>
    <div class="contact__lines">
      <p class="contact__line"><svg viewBox="0 0 16 16" aria-hidden="true"><path d="M4.5 1l2.5 3.5-1.6 1.4c.7 2 2.2 3.8 4.2 4.9l1.5-1.5L14.5 12l-2 2.5C7 14 2 9 1.8 3.2z"/></svg>555 310 7725</p>
      <p class="contact__line"><svg viewBox="0 0 16 16" aria-hidden="true"><path d="M0 3h16v10H0zm1.5 1.2L8 9l6.5-4.8V4h-13zm0 1.6V12h13V5.8L8 10.6z"/></svg>office@hartwellfloorco.com</p>
    </div>
  </div>
</section>

<section class="card card--back-appointment">
  <p class="watermark">quality first</p>
  <div class="slogan">
    <p><span class="slogan__lead">Hartwell</span><span class="slogan__line">flooring at</span></p>
    <p class="slogan__line">an affordable price</p>
  </div>
  <div class="appointment">
    <div class="appointment__field"><span>Date :</span><span class="appointment__blank"></span></div>
    <div class="appointment__field"><span>Time :</span><span class="appointment__blank"></span></div>
  </div>
  <p class="site-url">hartwellfloorco.com</p>
</section>

</body>
</html>
```